IT Consulting, IT Guru, Software Development, Network Solutions, Hosting

Attached is logo for our company, we just was the designers to come up with creative ideas to use the logo and the theme to come with creative and energetic business cards that leave an impression and stick in people's head.

Target Market(s)

Medical, Law, Entertainment, Real estate, any small to medium size business.

Industry/Entity Type

Business

Font styles to use
Serif
Sans Serif

```html
<!DOCTYPE html>
<html lang="en">
<head>
<meta charset="utf-8">
<title>Byteforge business card</title>
<link rel="stylesheet" href="https://fonts.googleapis.com/css2?family=Arimo:wght@400;700&display=swap">
<style>
  :root {
    --page-bg: #f1f1f1;
    --card-dark: #161c21;
    --card-yellow: #ffd200;
    --brand-white: #eef0f1;
    --ink-white: #ffffff;
    --caption: #333333;
  }
  * { margin: 0; padding: 0; box-sizing: border-box; }
  html, body { width: 1200px; height: 666px; overflow: hidden; }
  body {
    background: var(--page-bg);
    font-family: "Arimo", Arial, sans-serif;
  }
  .canvas {
    position: relative;
    width: 1200px;
    height: 666px;
  }
  .card-slot {
    position: absolute;
    top: 190px;
    width: 480px;
  }
  .card-slot--front { left: 90px; }
  .card-slot--back { left: 630px; }
  .card {
    position: relative;
    width: 480px;
    height: 267px;
    overflow: hidden;
  }
  .card--front {
    background: var(--card-dark);
    display: flex;
    align-items: center;
    justify-content: center;
  }
  .brand-name {
    color: var(--brand-white);
    font-weight: 400;
    font-size: 35px;
    letter-spacing: 1px;
  }
  .card--back { background: var(--card-yellow); color: var(--ink-white); }
  .headline {
    position: absolute;
    left: 34px;
    top: 52px;
    font-weight: 700;
    font-size: 50px;
    line-height: 56px;
    letter-spacing: -0.5px;
  }
  .contact {
    position: absolute;
    right: 14px;
    bottom: 18px;
    text-align: right;
    font-size: 20px;
    line-height: 22px;
    font-style: normal;
  }
  .caption {
    margin-top: 16px;
    text-align: center;
    font-size: 18px;
    color: var(--caption);
  }
</style>
</head>
<body>
  <main class="canvas">
    <section class="card-slot card-slot--front">
      <div class="card card--front">
        <span class="brand-name">BYTEFORGE</span>
      </div>
      <p class="caption">front</p>
    </section>
    <section class="card-slot card-slot--back">
      <div class="card card--back">
        <p class="headline">stuck on tech?<br>just ring us</p>
        <address class="contact">
          <span>Dana Reyes</span><br>
          <span>dana@byteforge.com</span><br>
          <span>55 412 906218</span>
        </address>
      </div>
      <p class="caption">back</p>
    </section>
  </main>
</body>
</html>
```